Belle Lueur Hand Crafted Candles promotional flyer

Hand Crafted Soy Candles - I need a flyer to promote my candles and to give information on care of candles.I want this to use the design and colours I already have for my labels and the photo I have attached.I am aiming at a sophisticated market so would like to reflect this in the design.
Should appeal to sophisticated women who enjoy the pleasure of candles - to enhance their enjoyment of life - gives them the 'Belle Lueur'.
the candles are hand crafted from all natural ingredients, environmentally friendly and with exquisite fragrances

Target Market(s)

sophisticated females

Industry/Entity Type

Promotional

Font styles to use
Script

Colors
cfeae6
ecdaeb

Requirements
Must have
• something expressing 'Belle Lueur' - the enjoyment of candles
Should not have
• bright colours

```html
<!DOCTYPE html>
<html lang="en">
<head>
<meta charset="utf-8">
<title>Belle Lueur Hand Crafted Candles – Flyer</title>
<link rel="stylesheet" href="https://fonts.googleapis.com/css2?family=Cinzel:wght@400;600;700&family=Parisienne&family=Lato:wght@400;700&display=swap">
<style>
  :root {
    --charcoal: #48484a;
    --mint: #9fd4cc;
    --mint-pale: #cfeae6;
    --mint-soft: #e6f4f2;
    --silver: #a9a7a8;
    --ink: #3d3d3f;
    --white: #ffffff;
    --page: #f2f2f2;
  }
  * { margin: 0; padding: 0; box-sizing: border-box; }
  html, body { width: 907px; height: 1200px; overflow: hidden; background: var(--page); }
  .flyer {
    position: relative; width: 907px; height: 1200px; overflow: hidden;
    background: var(--white); font-family: "Lato", sans-serif; color: var(--ink);
  }
  .flyer__shapes { position: absolute; inset: 0; }
  .pattern-area {
    position: absolute; left: 560px; top: 0; width: 347px; height: 520px;
    background: radial-gradient(ellipse at 70% 35%, var(--mint-soft) 0%, rgba(230,244,242,0.4) 55%, rgba(255,255,255,0) 80%);
  }
  .brand-seal {
    position: absolute; left: 43px; top: 15px; width: 328px; height: 328px; border-radius: 50%;
    background: var(--mint-soft); display: flex; flex-direction: column; align-items: center; justify-content: center;
  }
  .brand-seal__name { font-family: "Parisienne", cursive; font-size: 48px; color: var(--ink); line-height: 1; }
  .brand-seal__tag { font-family: "Cinzel", serif; font-size: 17px; color: var(--ink); margin-top: 14px; letter-spacing: 0.5px; }
  .headline { position: absolute; right: 30px; top: 150px; text-align: right; color: var(--charcoal); }
  .headline__script { font-family: "Parisienne", cursive; font-size: 50px; line-height: 1; margin-right: 6px; }
  .headline__line { font-family: "Cinzel", serif; font-weight: 600; font-size: 38px; line-height: 1.15; letter-spacing: 1px; }
  .headline__line--big { font-size: 50px; }
  .headline__line--huge { font-size: 84px; font-weight: 700; line-height: 1.05; }
  .features { position: absolute; left: 48px; top: 560px; width: 330px; list-style: none; }
  .features li { position: relative; padding-left: 24px; font-size: 17px; line-height: 1.3; margin-bottom: 10px; }
  .features li::before { content: ""; position: absolute; left: 0; top: 7px; width: 8px; height: 8px; border-radius: 50%; background: var(--charcoal); }
  .info { position: absolute; left: 455px; width: 420px; }
  .info--soy { top: 520px; }
  .info--refill { top: 842px; }
  .info__title { font-family: "Parisienne", cursive; font-weight: 400; font-size: 38px; color: var(--ink); margin-bottom: 10px; }
  .info__list { list-style: none; }
  .info__list li { position: relative; padding-left: 26px; font-size: 15.5px; line-height: 1.3; margin-bottom: 12px; }
  .info__list li::before { content: ""; position: absolute; left: 0; top: 5px; width: 9px; height: 9px; border-radius: 50%; background: var(--mint); }
  .candle-photo {
    position: absolute; left: -40px; top: 870px; width: 300px; height: 300px; border-radius: 50%;
    background: radial-gradient(circle at 55% 60%, #2f3135 0%, #5a5d62 35%, #c9cbcd 70%, #e4e5e6 100%);
  }
  .contact { position: absolute; left: 0; right: 0; top: 1122px; color: var(--white); font-size: 17px; }
  .contact__label { font-family: "Parisienne", cursive; font-size: 16px; opacity: 0.85; margin-right: 6px; }
  .contact__phone { position: absolute; left: 380px; top: 0; }
  .contact__email { position: absolute; right: 34px; top: 0; }
  .contact__web { position: absolute; left: 520px; top: 26px; }
</style>
</head>
<body>
<main class="flyer">
  <div class="pattern-area" role="img" aria-label="Faint floral pattern in pale mint"></div>

  <svg class="flyer__shapes" width="907" height="1200" viewBox="0 0 907 1200" aria-hidden="true">
    <defs>
      <linearGradient id="mintFade" x1="0" y1="0" x2="0" y2="1">
        <stop offset="0" stop-color="#9fd4cc"/>
        <stop offset="0.45" stop-color="#cfeae6"/>
        <stop offset="1" stop-color="#ffffff"/>
      </linearGradient>
      <linearGradient id="bandFade" x1="0" y1="0" x2="1" y2="0">
        <stop offset="0" stop-color="#9fd4cc"/>
        <stop offset="1" stop-color="#cfeae6"/>
      </linearGradient>
    </defs>
    <!-- side mint panel behind feature list -->
    <circle cx="40" cy="680" r="400" fill="url(#mintFade)"/>
    <path d="M0,500 C200,470 340,520 420,620 C470,690 450,800 360,860" fill="none" stroke="#a9a7a8" stroke-width="6"/>
    <!-- sweeping mint and silver bands -->
    <path d="M0,470 C260,430 520,470 700,520 C800,548 860,560 907,570 V620 C850,600 780,585 690,565 C500,520 260,490 0,525 Z" fill="url(#bandFade)"/>
    <path d="M0,462 C260,420 520,462 700,512 C800,540 860,552 907,560" fill="none" stroke="#a9a7a8" stroke-width="5"/>
    <path d="M120,530 C380,470 640,510 907,640" fill="none" stroke="#a9a7a8" stroke-width="3"/>
    <!-- charcoal top panel -->
    <path d="M0,0 H720 C600,150 430,360 0,445 Z" fill="#48484a"/>
    <path d="M720,0 C600,150 430,360 0,445" fill="none" stroke="#ffffff" stroke-width="6"/>
    <path d="M760,0 C640,170 470,380 0,460" fill="none" stroke="#a9a7a8" stroke-width="4"/>
    <path d="M907,0 V40 C860,20 820,10 790,0 Z" fill="#48484a"/>
    <!-- bottom charcoal band -->
    <path d="M0,1200 V1105 C320,1170 660,1120 907,990 V1200 Z" fill="#48484a"/>
    <path d="M160,1090 C420,1120 680,1080 907,960" fill="none" stroke="#cfeae6" stroke-width="12"/>
    <path d="M170,1100 C430,1132 690,1092 907,975" fill="none" stroke="#a9a7a8" stroke-width="5"/>
    <!-- ring around candle photo -->
    <circle cx="110" cy="1020" r="162" fill="#ffffff"/>
    <circle cx="110" cy="1020" r="170" fill="none" stroke="#9fd4cc" stroke-width="8"/>
  </svg>

  <div class="brand-seal">
    <span class="brand-seal__name">Belle Lueur</span>
    <span class="brand-seal__tag">Hand Crafted Soy Candles</span>
  </div>

  <header class="headline">
    <div class="headline__script">Belle Lueur</div>
    <div class="headline__line">An Exuberant</div>
    <div class="headline__line headline__line--big">Enjoyment</div>
    <div class="headline__line headline__line--huge">Of Life</div>
  </header>

  <ul class="features">
    <li>Candles are lovingly hand-poured and use only the finest of ingredients and fragrances</li>
    <li>Hand crafted soy candle creations</li>
    <li>Completely non-toxic</li>
    <li>Exquisite fragrances</li>
    <li>Clean burning</li>
    <li>Environmentally friendly</li>
  </ul>

  <section class="info info--soy">
    <h2 class="info__title">Why soy wax?</h2>
    <ul class="info__list">
      <li>Soft smooth wax that burns clear – no soot or smoke</li>
      <li>Soy wax candles burn up to 50% longer than traditional paraffin candles</li>
      <li>Made form soya beans, a renewable natural resource that supports and sustains agriculture it is biodegradable and environmentally friendly</li>
      <li>Soy wax burns cooler than paraffin and disperse the fragrance more fully.</li>
    </ul>
  </section>

  <section class="info info--refill">
    <h2 class="info__title">Containers can be refilled</h2>
    <ul class="info__list">
      <li>I offer a refill service - if you return you containers to me I can refill with the fragrance of your choice</li>
      <li>if you have a special container you would like to use for your candle just contact me for a quote.</li>
      <li>I have a wide range of fragrances - please contact me for details</li>
    </ul>
  </section>

  <div class="candle-photo" role="img" aria-label="Photo of a black glass soy candle jar with a pale round label"></div>

  <footer class="contact">
    <span class="contact__phone"><span class="contact__label">Call</span>021 555 0183</span>
    <span class="contact__email"><span class="contact__label">Email</span>hello@bellelueur.co.nz</span>
    <span class="contact__web"><span class="contact__label">Visit us -</span>www.bellelueur.co.nz</span>
  </footer>
</main>
</body>
</html>
```